Business Card for Lorena Whitfield

Name: Lorena Whitfield
Title: Realtor
Email: Lorena@LorenaWhitfieldRE.com
Phone: 480-555-0137

On the front of the business card, I would like the photo, the contact information and the Lorena Whitfield Logo. The backside is required to have the Broker logo and the required logos. Please use the colors from the logo design. Our company has a classy, professional look.

```html
<!DOCTYPE html>
<html lang="en">
<head>
<meta charset="utf-8">
<title>Lorena Whitfield – Business Card</title>
<link href="https://fonts.googleapis.com/css2?family=Montserrat:wght@700&family=Arimo:wght@400&display=swap" rel="stylesheet">
<style>
  :root {
    --bg: #c9c9c9;
    --card-white: #ffffff;
    --brand-red: #c8202f;
    --ink: #2b2b2b;
    --rule-grey: #8a8a8a;
    --card-dark: #4a4a4a;
    --mark-white: #ffffff;
  }
  * { margin: 0; padding: 0; box-sizing: border-box; }
  html, body { width: 1200px; height: 788px; overflow: hidden; }
  body {
    background: var(--bg);
    font-family: "Arimo", Arial, sans-serif;
    color: var(--ink);
    position: relative;
  }
  .card {
    position: absolute;
    left: 330px;
    width: 540px;
    height: 309px;
    border-radius: 18px;
    overflow: hidden;
  }
  .card--front { top: 64px; background: var(--card-white); }
  .card--back { top: 415px; background: var(--card-dark); }

  /* Front */
  .agent-photo {
    position: absolute;
    right: 0; top: 0;
    width: 250px; height: 309px;
    background: linear-gradient(180deg, #e8e8e8 0%, #bdbdbd 55%, #3a3a3a 100%);
  }
  .brand {
    position: absolute;
    left: 30px; top: 100px;
    display: flex; align-items: center; gap: 10px;
  }
  .brand__square {
    width: 30px; height: 30px;
    background: var(--brand-red);
    flex: none;
  }
  .brand__name {
    font-family: "Arimo", Arial, sans-serif;
    font-weight: 400;
    font-size: 17px;
    line-height: 1.25;
    color: var(--brand-red);
  }
  .brand__rule {
    position: absolute;
    left: 70px; top: 154px;
    width: 190px; height: 1px;
    background: var(--rule-grey);
  }
  .agent {
    position: absolute;
    left: 0; top: 196px;
    padding-left: 30px;
    border-left: 8px solid var(--brand-red);
  }
  .agent__name {
    font-family: "Montserrat", Arial, sans-serif;
    font-weight: 700;
    font-size: 19px;
    letter-spacing: 1px;
    color: var(--brand-red);
    text-transform: uppercase;
  }
  .agent__title { font-size: 13px; margin-top: 1px; }
  .contact {
    position: absolute;
    left: 38px; top: 248px;
    list-style: none;
    font-size: 13px;
    line-height: 21px;
  }
  .contact li { display: flex; align-items: center; gap: 7px; }
  .contact svg { width: 10px; height: 10px; fill: var(--brand-red); }

  /* Back */
  .compliance {
    position: absolute;
    left: 0; right: 0; top: 104px;
    display: flex; align-items: center; justify-content: center; gap: 16px;
  }
  .badge { border: 3px solid var(--mark-white); }
  .badge--housing { width: 62px; height: 62px; }
  .badge--listing { width: 130px; height: 52px; }
  .divider { width: 1px; height: 82px; background: var(--mark-white); opacity: .8; }
  .broker {
    display: flex; flex-direction: column; align-items: center; gap: 6px;
    color: var(--mark-white);
    font-family: "Arimo", Arial, sans-serif;
    font-weight: 400;
    text-align: center;
  }
  .broker__circle { width: 44px; height: 44px; border-radius: 50%; border: 2px solid var(--mark-white); }
  .broker__name { font-size: 12px; line-height: 1.3; }
</style>
</head>
<body>
  <section class="card card--front">
    <div class="agent-photo" role="img" aria-label="Black and white portrait photo of the realtor"></div>
    <div class="brand">
      <span class="brand__square"></span>
      <span class="brand__name">Lorena Whitfield<br>Real Estate</span>
    </div>
    <div class="brand__rule"></div>
    <div class="agent">
      <div class="agent__name">Lorena Whitfield</div>
      <div class="agent__title">Realtor</div>
    </div>
    <ul class="contact">
      <li>
        <svg viewBox="0 0 10 10"><path d="M2 0 L4 2.5 L3 3.6 Q4.5 6 6.4 7 L7.5 6 L10 8 L8.5 10 Q2 9 0 1.5 Z"/></svg>
        480-555-0137
      </li>
      <li>
        <svg viewBox="0 0 10 10"><path d="M0 2 H10 V8 H0 Z M0 2 L5 5.5 L10 2" stroke="#fff" stroke-width=".8"/></svg>
        Lorena@LorenaWhitfieldRE.com
      </li>
    </ul>
  </section>

  <section class="card card--back">
    <div class="compliance">
      <div class="badge badge--housing" role="img" aria-label="Fair housing badge"></div>
      <div class="divider"></div>
      <div class="badge badge--listing" role="img" aria-label="Realtor and listing service badge"></div>
      <div class="divider"></div>
      <div class="broker">
        <span class="broker__circle"></span>
        <span class="broker__name">Harlan Reed<br>Real Estate</span>
      </div>
    </div>
  </section>
</body>
</html>
```